Newsletter March April 2020

create a newsletter to send to client which is informative and visually impactful

previous projects attached

Target Market(s)

property market

Industry/Entity Type

Property

Colors
abd037

Requirements
Must have
• company logo
www.veltrampage.co.uk
Nice to have
• colour inline with logo etc
graphics to show data where possible

```html
<!DOCTYPE html>
<html lang="en">
<head>
<meta charset="utf-8">
<title>Veltram Page – March–April 2020 Newsletter</title>
<link href="https://fonts.googleapis.com/css2?family=Arimo:ital,wght@0,400;0,700;1,400&display=swap" rel="stylesheet">
<style>
  :root {
    --green: #3dd13d;
    --green-mid: #2fb52f;
    --green-deep: #1e8f1e;
    --green-dark: #063806;
    --ink: #111;
    --ink-soft: #2b2b2b;
    --grey: #c9c9c9;
    --white: #fff;
  }
  * { margin: 0; padding: 0; box-sizing: border-box; }
  html, body { width: 1200px; height: 776px; overflow: hidden; background: var(--white); }
  body { position: relative; font-family: "Arimo", Arial, sans-serif; }

  .page {
    position: absolute; top: 34px; width: 548px; height: 708px;
    background: var(--green); overflow: hidden;
    box-shadow: 0 0 14px rgba(90, 230, 90, .55);
  }
  .page--back { left: 32px; }
  .page--front { left: 620px; overflow: visible; }

  .page-corner { position: absolute; top: 0; right: 0; width: 80px; height: 80px; }
  .page-number { position: absolute; top: 14px; right: 16px; color: var(--white); font-weight: 700; font-size: 20px; }

  /* back page */
  .article-title { position: absolute; left: 26px; top: 46px; width: 430px; font-size: 19px; font-weight: 700; color: var(--ink); line-height: 25px; letter-spacing: .5px; }
  .intro-bar { position: absolute; left: 26px; top: 110px; width: 18px; height: 100px; background: var(--green-dark); }
  .body-text { position: absolute; font-size: 10.8px; line-height: 12.8px; color: var(--white); text-align: justify; letter-spacing: .3px; }
  .intro-text { left: 58px; top: 125px; width: 463px; }
  .lamp-photo { position: absolute; left: 26px; top: 219px; width: 496px; height: 154px;
    background: radial-gradient(ellipse at 40% 55%, #5a5e5c 0%, #2a2d2c 35%, #111312 75%); }
  .case-band { position: absolute; left: 26px; top: 375px; width: 372px; height: 43px; }
  .case-band svg { position: absolute; inset: 0; }
  .case-label { position: absolute; left: 5px; top: 13px; font-size: 14.4px; color: var(--ink); letter-spacing: .4px; }
  .case-label b { margin-right: 9px; }
  .case-text { left: 26px; top: 427px; width: 496px; }

  .result-band { position: absolute; left: 0; top: 476px; width: 548px; height: 79px; background: var(--green-dark); }
  .rating-table { position: absolute; left: 30px; top: 6px; color: var(--white); font-size: 12px; border-collapse: collapse; table-layout: fixed; width: 262px; }
  .rating-table th, .rating-table td { text-align: left; font-weight: 400; padding: 0; height: 25px; white-space: nowrap; }
  .rating-table th { height: 22px; }
  .rating-table .row-label { width: 59px; }
  .rating-table .col-software { width: 107px; padding-left: 19px; border-left: 1px solid var(--green); }
  .rating-table .col-rating { width: 96px; }
  .rating-table thead .col-software, .rating-table thead .col-rating { border-bottom: 1px solid var(--green); }
  .result-callout { position: absolute; left: 316px; top: 8px; width: 232px; height: 62px; }
  .result-callout svg { position: absolute; inset: 0; }
  .result-text { position: absolute; left: 62px; top: 12px; width: 140px; font-size: 12px; font-weight: 700; color: var(--ink-soft); text-align: center; line-height: 13px; letter-spacing: .8px; }
  .closing-text { left: 26px; top: 565px; width: 496px; }

  .site-footer { position: absolute; left: 0; top: 651px; width: 548px; height: 57px; background: var(--green-dark);
    display: flex; align-items: center; justify-content: center; gap: 8px; color: var(--white); font-size: 12px; letter-spacing: .3px; }

  /* front page */
  .hero-photo { position: absolute; left: 0; top: 0; width: 548px; height: 404px;
    background: radial-gradient(ellipse at 35% 25%, #f1f3ec 0%, #dfe6d2 35%, #b7c59a 65%, #6c7d4a 100%); }
  .brand { position: absolute; left: 27px; top: 26px; display: flex; align-items: center; gap: 7px;
    font-size: 28px; font-weight: 700; color: #3a3a3a; letter-spacing: -.5px; }
  .brand-dot { width: 16px; height: 16px; border-radius: 50%; background: var(--green-deep); }
  .issue-title { position: absolute; left: 27px; top: 80px; font-size: 37px; font-weight: 700; color: #2a2a2a; letter-spacing: .3px; }
  .issue-banner { position: absolute; left: -8px; top: 122px; width: 418px; height: 34px; }
  .issue-banner svg { position: absolute; inset: 0; }
  .issue-date { position: absolute; left: 35px; top: 8px; font-size: 14.4px; font-style: italic; color: var(--white); }
  .issue-tagline { position: absolute; left: 27px; top: 160px; font-size: 28px; color: var(--green-deep); letter-spacing: .3px; }
  .front-lower { position: absolute; left: 0; top: 404px; width: 548px; height: 304px;
    background: linear-gradient(180deg, var(--green-dark) 0 12px, var(--green) 12px, var(--green-mid) 100%); }
  .front-text { left: 27px; top: 438px; width: 233px; font-size: 11px; letter-spacing: .2px; }
  .front-text p + p { margin-top: 12.8px; }
  .contents-box { position: absolute; left: 294px; top: 438px; width: 235px; height: 246px;
    background: var(--green-dark); border: 1.5px solid #6be86b; color: var(--white); }
  .contents-text { position: absolute; left: 9px; width: 214px; font-size: 10px; line-height: 12.8px; text-align: justify; }
  .contents-rule { position: absolute; left: 10px; width: 140px; height: 2px; background: var(--green-deep); }
  .contents-page { position: absolute; left: 141px; width: 83px; height: 26px; background: var(--green);
    color: var(--ink); font-weight: 700; font-size: 12px; letter-spacing: .5px; display: flex; align-items: center; justify-content: center; }
</style>
</head>
<body>

<section class="page page--back">
  <svg class="page-corner" viewBox="0 0 80 80"><polygon points="0,0 80,0 80,80" fill="var(--green-dark)"/></svg>
  <span class="page-number">4</span>

  <h2 class="article-title">Comparing 2009 EPC vs 2019/2020 EPC ratings – Why are they different?</h2>
  <div class="intro-bar"></div>
  <p class="body-text intro-text">The software and conventions adhered to by energy assessors has changed significantly over the past 10 years. Energy assessors will now capture far more details from a site inspection, and with the introduction of new technologies and improvements in LED lighting, a band C property assessed 10 years ago, with no changes, may re calculate at a different band today.</p>

  <div class="lamp-photo" role="img" aria-label="Photograph of pendant LED lamps hanging from a dark warehouse ceiling"></div>

  <div class="case-band">
    <svg viewBox="0 0 372 43" preserveAspectRatio="none"><polygon points="0,0 372,0 348,43 0,43" fill="var(--green-mid)"/></svg>
    <span class="case-label"><b>Case Study:</b>300m2 Industrial Warehouse Unit.</span>
  </div>
  <p class="body-text case-text">Calculating the same building using todays software (nBEAM 5.6a) against software used 10 years ago (nBEAM 3.4a) calculates a different rating despite the same details being entered.</p>

  <div class="result-band">
    <table class="rating-table">
      <thead>
        <tr><th class="row-label"></th><th class="col-software">Software</th><th class="col-rating">Rating</th></tr>
      </thead>
      <tbody>
        <tr><td class="row-label">Previous</td><td class="col-software">nBEAM 3.4a</td><td class="col-rating">Band D 89</td></tr>
        <tr><td class="row-label">Current</td><td class="col-software">nBEAM 5.6a</td><td class="col-rating">Band E 101</td></tr>
      </tbody>
    </table>
    <div class="result-callout">
      <svg viewBox="0 0 232 62" preserveAspectRatio="none"><polygon points="32,0 232,0 232,62 0,62" fill="var(--grey)"/></svg>
      <p class="result-text">The result is a lower banding for the building.</p>
    </div>
  </div>

  <p class="body-text closing-text">Over the past 10 years each software release has made small changes to how data is input and calculated. Recent updates have included changes to luminous efficacy of LED lamps. Previous versions had LED lamps at a similar efficiency to T5 florescent lamps, now a greater efficacy has been assigned. Therefore a building with LED lamps could have a potentially better asset rating with the latest software update compared to previous versions.</p>

  <footer class="site-footer">
    <svg width="16" height="16" viewBox="0 0 16 16" fill="none" stroke="#fff" stroke-width="1">
      <circle cx="8" cy="8" r="7"/><ellipse cx="8" cy="8" rx="3" ry="7"/><line x1="1" y1="8" x2="15" y2="8"/><line x1="2.2" y1="4.5" x2="13.8" y2="4.5"/><line x1="2.2" y1="11.5" x2="13.8" y2="11.5"/>
    </svg>
    <span>https://www.veltrampage.co.uk</span>
  </footer>
</section>

<section class="page page--front">
  <div class="hero-photo" role="img" aria-label="Photograph of a small wooden model house resting on a stone, in soft green tones"></div>
  <svg class="page-corner" viewBox="0 0 80 80"><polygon points="0,0 80,0 80,80" fill="var(--green-dark)"/></svg>
  <span class="page-number">1</span>

  <div class="brand"><span>VELTRAM PAGE</span><span class="brand-dot"></span></div>
  <h1 class="issue-title">COVID – 19 and EPCs</h1>
  <div class="issue-banner">
    <svg viewBox="0 0 418 34" preserveAspectRatio="none"><polygon points="0,0 418,0 384,34 0,34" fill="var(--green-deep)"/></svg>
    <span class="issue-date">March - April (2020) Newsletter v3(002)</span>
  </div>
  <p class="issue-tagline">Keeping Transaction going</p>

  <div class="front-lower"></div>
  <div class="body-text front-text">
    <p>In the current situation with Coronavirus and issues with access to certain sites, Veltram Page have come up with a solution to provide draft EPCs based on a property proforma which we can provide without going to site.</p>
    <p>If there are lease or sale transactions where there are difficulties with access, we have agreed with accrediting bodies that we are able to provide a draft then evidence site visit and lodgement when access can later be provided. This therefore does not hold up transactions in cases where it may previously have done so.</p>
    <p>If you have any transactions that maybe held up due to EPCs, please let us know.</p>
  </div>

  <nav class="contents-box">
    <p class="contents-text" style="top:12px">Domestic EPC - Minimum energy efficiency standards rollout to existing tenancies from April 2020</p>
    <div class="contents-rule" style="top:76px"></div>
    <span class="contents-page" style="top:53px">Page 2</span>

    <p class="contents-text" style="top:100px">Upcoming changes</p>
    <div class="contents-rule" style="top:140px"></div>
    <span class="contents-page" style="top:117px">Page 3</span>

    <p class="contents-text" style="top:176px">Comparing 2009 EPC vs 2019/2020 EPC ratings – Why are they different?</p>
    <div class="contents-rule" style="top:230px"></div>
    <span class="contents-page" style="top:207px">Page 4</span>
  </nav>
</section>

</body>
</html>
```